Visitenkarten-Design für Psychiaterin
Zielgruppe
Dr. med. Monika Haberl, Ärztin, Psychotherapie für Kinder Jugendliche und Erwachsene, spezialisiert auf komplexe Posttraumatische Belastungsstörung, Dissoziative Störungen, Persönlichkeitsstörungen, Bindungsstörungen, LUMO-Mentorin
Das Design soll modern sein, Seriosität Professionalität, Dynamik und Geborgenheit ausstrahlen. Zielgruppe sind Menschen die traumatische Situationen überlebt haben.
Aufgabenstellung
Name, Fachgebiet und Spezialisierung, Telefonnummer, e-Mail
Unter Dateiupload sind Visitenkartenbeispiele die mir gefallen

```html
<!DOCTYPE html>
<html lang="de">
<head>
<meta charset="utf-8">
<title>Visitenkarte Dr. med. Monika Haberl</title>
<link rel="stylesheet" href="https://fonts.googleapis.com/css2?family=Questrial&family=Poppins:wght@600&display=swap">
<style>
  :root {
    --teal: #5fb4c1;
    --teal-light: #aad9df;
    --ink: #3b4450;
    --ink-soft: #4a525c;
    --paper: #ffffff;
    --stage: #ffffff;
  }
  * { margin: 0; padding: 0; box-sizing: border-box; }
  html, body {
    width: 1200px; height: 854px; overflow: hidden;
    background: var(--stage);
  }
  .canvas { position: relative; width: 1200px; height: 854px; }
  .card {
    position: absolute; top: 37px; width: 518px; height: 800px;
    background: var(--paper); border-radius: 40px; overflow: hidden;
    box-shadow: 0 4px 18px rgba(0,0,0,0.14);
    font-family: "Questrial", "Century Gothic", sans-serif;
    color: var(--ink-soft);
  }
  .card--front { left: 19px; }
  .card--back { left: 647px; }
  .card__band {
    position: absolute; left: 0; top: 0; width: 100%; height: 336px;
    background: linear-gradient(to bottom, var(--teal) 0%, var(--teal) 88%, var(--paper) 100%);
  }
  .card__emblem {
    position: absolute; top: 67px; width: 258px; height: 269px;
    border-radius: 130px 130px 30px 30px;
    background: radial-gradient(ellipse at 45% 35%, #ffffff 0%, #f4fafb 45%, var(--teal-light) 100%);
  }
  .card--front .card__emblem { left: 104px; }
  .card--back .card__emblem { left: 156px; }
  .card__content { position: absolute; left: 82px; top: 386px; right: 20px; }
  .title { font-size: 38px; line-height: 40px; color: var(--ink); }
  .name {
    font-family: "Poppins", "Century Gothic", sans-serif; font-weight: 600;
    font-size: 50px; line-height: 54px; color: var(--ink); letter-spacing: -0.5px;
  }
  .field { margin-top: 20px; font-size: 24px; letter-spacing: 5.5px; color: var(--ink); }
  .audience { margin-top: 2px; font-size: 23.5px; color: var(--teal); }
  .focus-list { margin-top: 20px; list-style: none; font-size: 24px; line-height: 27px; }
  .focus-list li { position: relative; padding-left: 22px; }
  .focus-list li::before {
    content: ""; position: absolute; left: 2px; top: 11px;
    width: 8px; height: 8px; border-radius: 50%; background: var(--teal);
  }
  .contact { margin-top: 34px; font-size: 27.5px; line-height: 32px; padding-left: 4px; }
  .contact__block + .contact__block { margin-top: 32px; }
  .contact__web { color: var(--teal); font-size: 26px; }
</style>
</head>
<body>
<main class="canvas">
  <section class="card card--front">
    <div class="card__band"></div>
    <div class="card__emblem" role="img" aria-label="Illustration: Kopfsilhouette im Profil mit Netzwerk aus farbigen Kreisen und Punkten"></div>
    <div class="card__content">
      <p class="title">Dr. med.</p>
      <h1 class="name">Monika Haberl</h1>
      <p class="field">PSYCHOTHERAPIE</p>
      <p class="audience">Kinder | Jugendliche | Erwachsene</p>
      <ul class="focus-list">
        <li>Komplexe posttraumatische<br>Belastungsstörungen</li>
        <li>Dissoziative Störungen</li>
        <li>Persönlichkeitsstörungen</li>
        <li>Bindungsstörungen</li>
        <li>LUMO-Mentorin</li>
      </ul>
    </div>
  </section>

  <section class="card card--back">
    <div class="card__band"></div>
    <div class="card__emblem" role="img" aria-label="Illustration: Kopfsilhouette im Profil mit Netzwerk aus farbigen Kreisen und Punkten"></div>
    <div class="card__content">
      <p class="title">Dr. med.</p>
      <h2 class="name">Monika Haberl</h2>
      <div class="contact">
        <p class="contact__block">Lindenallee 27<br>79104 Birkenfeld</p>
        <p class="contact__block">Fon 07612 483915<br>Fax 07612 483916<br>haberl@praxis-lindenhof.de<br><span class="contact__web">www.praxis-lindenhof.de</span></p>
      </div>
    </div>
  </section>
</main>
</body>
</html>
```